Additional Technology ICONS for Web project

We have a group of ICONS from one part of the business, and we need some new ICONS generated for other components. We are a telecommunications company with a web portal, and we have ICONS for our hosting products, but not data or voice services.

We require, in the existing ICON Format, a graphic which represents the following:

The Data LOB groups are:
- IP/VPN (e.g. point to point arrow connections)
- Internet
- Voice Services (Telephone)
- Management (control/hands)
- Other (can use same as Hosting)

For voice:
- ISDN (PABX Like)
- PSTN (Telephone Like)
- Inbound (lots of telephones making calls in)

For mobiles:
- Voice (a Mobile)
- Data (Mobile Data) (Phone with Network connection)

The time is set to 2 days, as we are short of time, but I may extend a day to Monday.

Reason: Hi, Some very good designs here, but I need to extend to Monday, so I can give feedback to everyone.

Target Market(s)

Corporate/Business.

Industry/Entity Type

Telecommunications

Requirements
Must have
• The Colour, Circle Style must be the same as the existing hosting icons (see attached full sample, as well as the exact ICONS at the bottom). Only the graphic is the circle needs to change.

example format is to be: Each ICON in the complete blue square background, and darkblue circle/white inside graphic (e.g the cloud) with Text for the demo.

The final delivery needs to be: Each ICON witth the Blue (not selected) and a SECOND ICON INVERTED (Selected) format. No Text, similiar to the attached.
Nice to have
• simple, clean graphics
Should not have
• any other colours.

```html
<!DOCTYPE html>
<html lang="en">
<head>
<meta charset="utf-8">
<title>Service Icon Sets</title>
<link rel="stylesheet" href="https://fonts.googleapis.com/css2?family=Open+Sans:wght@400;600&display=swap">
<style>
  :root {
    --header-fill: #5b9bd5;
    --header-edge: #41719c;
    --panel-fill: #c3daf0;
    --row-divider: #e3eef9;
    --icon-fill: #2b2a86;
    --link-line: #3f79b8;
    --label-blue: #2e75b6;
    --label-hosting: #3b5a9a;
    --label-muted: #5b5b66;
    --page: #ffffff;
  }
  * { box-sizing: border-box; margin: 0; padding: 0; }
  html, body { width: 1200px; height: 1000px; overflow: hidden; background: var(--page); }
  body { position: relative; font-family: "Open Sans", Arial, sans-serif; }

  .category-header {
    position: absolute; top: 206px; width: 211px; height: 49px;
    background: var(--header-fill); border: 1px solid var(--header-edge);
    color: #fff; font-size: 20px; display: flex; align-items: center; justify-content: center;
  }
  .category-header.hosting { left: 98px; }
  .category-header.data { left: 342px; }
  .category-header.voice { left: 626px; }
  .category-header.mobile { left: 912px; }

  .icon-menu {
    position: absolute; list-style: none;
    background: linear-gradient(to right, var(--panel-fill) 82%, #ffffff);
  }
  .icon-menu.hosting { left: 130px; top: 268px; width: 130px; background: var(--panel-fill); }
  .icon-menu.data { left: 368px; top: 276px; width: 162px; padding-top: 6px; }
  .icon-menu.voice { left: 651px; top: 276px; width: 166px; padding-top: 2px; }
  .icon-menu.mobile { left: 932px; top: 276px; width: 164px; padding-top: 6px; }

  .menu-item {
    position: relative; display: flex; align-items: center;
    border-bottom: 1px solid var(--row-divider);
  }
  .menu-item:last-child { border-bottom: none; }
  .menu-item.is-selected { background: #fff; margin-left: 9px; }
  .menu-item svg { position: relative; z-index: 2; flex: none; }

  .hosting .menu-item { height: 59.5px; padding-left: 10px; gap: 8px; }
  .hosting .menu-item.is-selected { padding-left: 1px; }
  .hosting .label { font-size: 11px; font-weight: 600; color: var(--label-hosting); }
  .hosting .is-selected .label { color: var(--label-muted); font-weight: 400; }

  .data .menu-item { height: 59px; padding-left: 14px; gap: 13px; }
  .data .menu-item.is-selected { padding-left: 5px; }
  .voice .menu-item { height: 59.5px; padding-left: 18px; gap: 12px; }
  .voice .menu-item.is-selected { padding-left: 9px; }
  .mobile .menu-item { height: 59.5px; padding-left: 16px; gap: 12px; }
  .mobile .menu-item.is-selected { padding-left: 7px; }
  .data .label, .voice .label, .mobile .label { font-size: 12px; color: var(--label-blue); }

  .link-line { position: absolute; width: 4px; background: var(--link-line); z-index: 1; }
  .hosting .link-line { left: 26px; top: 30px; height: 240px; }
  .data .link-line { left: 30px; top: 36px; height: 116px; }
</style>
</head>
<body>

<div class="category-header hosting">Hosting</div>
<div class="category-header data">Data</div>
<div class="category-header voice">Voice</div>
<div class="category-header mobile">Mobile</div>

<!-- Hosting -->
<ul class="icon-menu hosting">
  <li class="link-line" aria-hidden="true"></li>
  <li class="menu-item">
    <svg width="36" height="36" viewBox="0 0 36 36"><circle cx="18" cy="18" r="17" fill="var(--icon-fill)"/><path d="M10 23a4 4 0 0 1 1-8 6 6 0 0 1 11-2 5 5 0 0 1 4 10z" fill="#fff"/></svg>
    <span class="label">Internet</span>
  </li>
  <li class="menu-item">
    <svg width="36" height="36" viewBox="0 0 36 36"><circle cx="18" cy="18" r="17" fill="var(--icon-fill)"/><path d="M12 11h12v5h3v10H9V16h3z" fill="#fff"/><path d="M12 20v4M15 20v4M18 20v4M21 20v4M24 20v4" stroke="var(--icon-fill)" stroke-width="1.3"/></svg>
    <span class="label">Network</span>
  </li>
  <li class="menu-item is-selected">
    <svg width="36" height="36" viewBox="0 0 36 36"><rect x="10" y="8" width="16" height="12" rx="1" fill="none" stroke="var(--icon-fill)" stroke-width="2.2"/><path d="M18 20v5M11 27h14" stroke="var(--icon-fill)" stroke-width="2.4"/></svg>
    <span class="label">Compute</span>
  </li>
  <li class="menu-item">
    <svg width="36" height="36" viewBox="0 0 36 36"><circle cx="18" cy="18" r="17" fill="var(--icon-fill)"/><ellipse cx="18" cy="11" rx="8" ry="3" fill="#fff"/><path d="M10 13.5c0 4 16 4 16 0v3.5c0 4-16 4-16 0zM10 19.5c0 4 16 4 16 0V23c0 4-16 4-16 0z" fill="#fff"/></svg>
    <span class="label">Storage</span>
  </li>
  <li class="menu-item">
    <svg width="36" height="36" viewBox="0 0 36 36"><circle cx="18" cy="18" r="17" fill="var(--icon-fill)"/><rect x="11" y="9" width="14" height="18" fill="#fff"/><path d="M13 12.5h10M13 16h10M13 19.5h10M13 23h10" stroke="var(--icon-fill)" stroke-width="1.4"/></svg>
    <span class="label">Co-location</span>
  </li>
  <li class="menu-item">
    <svg width="36" height="36" viewBox="0 0 36 36"><circle cx="18" cy="18" r="17" fill="var(--icon-fill)"/><rect x="9" y="12" width="18" height="12" rx="3" fill="#fff"/><circle cx="13.5" cy="18" r="1.5" fill="var(--icon-fill)"/><circle cx="18" cy="18" r="1.5" fill="var(--icon-fill)"/><circle cx="22.5" cy="18" r="1.5" fill="var(--icon-fill)"/></svg>
    <span class="label">Other</span>
  </li>
</ul>

<!-- Data -->
<ul class="icon-menu data">
  <li class="link-line" aria-hidden="true"></li>
  <li class="menu-item">
    <svg width="36" height="36" viewBox="0 0 36 36"><circle cx="18" cy="18" r="17" fill="var(--icon-fill)"/><path d="M10 23a4 4 0 0 1 1-8 6 6 0 0 1 11-2 5 5 0 0 1 4 10z" fill="#fff"/></svg>
    <span class="label">Internet</span>
  </li>
  <li class="menu-item">
    <svg width="36" height="36" viewBox="0 0 36 36"><circle cx="18" cy="18" r="17" fill="var(--icon-fill)"/><circle cx="7.5" cy="18" r="2.2" fill="#fff"/><circle cx="28.5" cy="18" r="2.2" fill="#fff"/><path d="M11 18h12M19.5 14.5 23 18l-3.5 3.5" stroke="#fff" stroke-width="1.8" fill="none"/></svg>
    <span class="label">IPVPN</span>
  </li>
  <li class="menu-item is-selected">
    <svg width="36" height="36" viewBox="0 0 36 36"><circle cx="18" cy="18" r="17" fill="var(--icon-fill)"/><circle cx="18" cy="13" r="4.5" fill="#fff"/><path d="M9 29c0-6 4-9 9-9s9 3 9 9z" fill="#fff"/><path d="M18 20.5v5" stroke="var(--icon-fill)" stroke-width="1.6"/></svg>
    <span class="label">Management</span>
  </li>
  <li class="menu-item">
    <svg width="36" height="36" viewBox="0 0 36 36"><circle cx="18" cy="18" r="17" fill="var(--icon-fill)"/><path d="M14 9h3l1 5-2.2 1.5a11 11 0 0 0 4 5L22 18l5 1v3c0 1.5-1.5 3-4 2.5-6-1.5-10.5-6-12-12 0-2 1.5-3.5 3-3.5z" fill="#fff" transform="rotate(12 18 18)"/></svg>
    <span class="label">Voice Services</span>
  </li>
  <li class="menu-item">
    <svg width="36" height="36" viewBox="0 0 36 36"><circle cx="18" cy="18" r="17" fill="var(--icon-fill)"/><rect x="9" y="12" width="18" height="12" rx="3" fill="#fff"/><circle cx="13.5" cy="18" r="1.5" fill="var(--icon-fill)"/><circle cx="18" cy="18" r="1.5" fill="var(--icon-fill)"/><circle cx="22.5" cy="18" r="1.5" fill="var(--icon-fill)"/></svg>
    <span class="label">Other</span>
  </li>
</ul>

<!-- Voice -->
<ul class="icon-menu voice">
  <li class="menu-item">
    <svg width="36" height="36" viewBox="0 0 36 36"><circle cx="18" cy="18" r="17" fill="var(--icon-fill)"/><rect x="14" y="8" width="8" height="6" fill="#fff"/><path d="M18 14v4M11 18h14M11 18v4M25 18v4M18 18v4" stroke="#fff" stroke-width="1.4" fill="none"/><rect x="8" y="22" width="6" height="5" fill="#fff"/><rect x="15" y="22" width="6" height="5" fill="#fff"/><rect x="22" y="22" width="6" height="5" fill="#fff"/></svg>
    <span class="label">ISDN</span>
  </li>
  <li class="menu-item">
    <svg width="36" height="36" viewBox="0 0 36 36"><circle cx="18" cy="18" r="17" fill="var(--icon-fill)"/><circle cx="18" cy="11" r="5" fill="none" stroke="#fff" stroke-width="1.5"/><path d="M16 9h1l.5 2-1 .6a4 4 0 0 0 1.5 1.6l.6-1 2 .4v1c0 .6-.6 1-1.4.9a5 5 0 0 1-4-4c0-.6.4-1 .8-1z" fill="#fff"/><path d="M18 16v4M11 20h14M11 20v3M25 20v3" stroke="#fff" stroke-width="1.4" fill="none"/><path d="M9 23h4l-.5 4h-3zM23 23h4l-.5 4h-3z" fill="#fff"/></svg>
    <span class="label">PSTN</span>
  </li>
  <li class="menu-item is-selected">
    <svg width="36" height="36" viewBox="0 0 36 36"><circle cx="18" cy="18" r="17" fill="var(--icon-fill)"/><circle cx="18" cy="18" r="14.5" fill="none" stroke="#fff" stroke-width="1"/><path d="M11 10h2.5l.8 4-1.6 1a8 8 0 0 0 2.6 4l1.2-1.4 3.5 1V21c0 1-1 2-2.6 1.7-4.5-1.3-7.5-5-8.5-9.5 0-1.6 1-3.2 2.1-3.2z" fill="#fff"/><path d="M27 12l-5 3M27 18h-5M27 24l-5-3" stroke="#fff" stroke-width="1.4"/></svg>
    <span class="label">Inbound</span>
  </li>
  <li class="menu-item">
    <svg width="36" height="36" viewBox="0 0 36 36"><circle cx="18" cy="18" r="17" fill="var(--icon-fill)"/><rect x="9" y="12" width="18" height="12" rx="3" fill="#fff"/><circle cx="13.5" cy="18" r="1.5" fill="var(--icon-fill)"/><circle cx="18" cy="18" r="1.5" fill="var(--icon-fill)"/><circle cx="22.5" cy="18" r="1.5" fill="var(--icon-fill)"/></svg>
    <span class="label">Other</span>
  </li>
</ul>

<!-- Mobile -->
<ul class="icon-menu mobile">
  <li class="menu-item">
    <svg width="36" height="36" viewBox="0 0 36 36"><circle cx="18" cy="18" r="17" fill="var(--icon-fill)"/><rect x="12" y="7" width="12" height="22" rx="2" fill="#fff"/><rect x="14" y="9.5" width="8" height="6" fill="var(--icon-fill)"/><g fill="var(--icon-fill)"><rect x="14" y="17.5" width="2" height="2"/><rect x="17" y="17.5" width="2" height="2"/><rect x="20" y="17.5" width="2" height="2"/><rect x="14" y="21" width="2" height="2"/><rect x="17" y="21" width="2" height="2"/><rect x="20" y="21" width="2" height="2"/><rect x="14" y="24.5" width="2" height="2"/><rect x="17" y="24.5" width="2" height="2"/><rect x="20" y="24.5" width="2" height="2"/></g></svg>
    <span class="label">Voice</span>
  </li>
  <li class="menu-item">
    <svg width="36" height="36" viewBox="0 0 36 36"><circle cx="18" cy="18" r="17" fill="var(--icon-fill)"/><g fill="none" stroke="#fff" stroke-width="2.2" stroke-linecap="round"><path d="M7 16a15 15 0 0 1 22 0"/><path d="M10.5 19.5a10 10 0 0 1 15 0"/><path d="M14 23a5 5 0 0 1 8 0"/></g><circle cx="18" cy="26.5" r="2.6" fill="#fff"/></svg>
    <span class="label">Data</span>
  </li>
  <li class="menu-item is-selected">
    <svg width="36" height="36" viewBox="0 0 36 36"><circle cx="18" cy="18" r="17" fill="var(--icon-fill)"/><rect x="9" y="12" width="18" height="12" rx="3" fill="#fff"/><circle cx="13.5" cy="18" r="1.5" fill="var(--icon-fill)"/><circle cx="18" cy="18" r="1.5" fill="var(--icon-fill)"/><circle cx="22.5" cy="18" r="1.5" fill="var(--icon-fill)"/></svg>
    <span class="label">Other</span>
  </li>
</ul>

</body>
</html>
```